RK Bastone Construction Inc.

Design a new business card for our construction company
To be removed from current card:
Delete 25 years
Delete Tenant fit up Renovations section

```html
<!DOCTYPE html>
<html lang="en">
<head>
<meta charset="utf-8">
<title>RK Bastone Construction Inc. – Business Card</title>
<link rel="stylesheet" href="https://fonts.googleapis.com/css2?family=Krona+One&family=Poppins:wght@400;500;800&display=swap">
<style>
  :root {
    --stage: #1f1f21;
    --card-white: #ffffff;
    --teal: #24786d;
    --purple: #4b2a78;
    --ink: #1b1b1b;
    --rule: #8a8a8a;
  }
  * { box-sizing: border-box; margin: 0; padding: 0; }
  html, body {
    width: 1200px; height: 900px; overflow: hidden;
    background: var(--stage);
    font-family: "Poppins", sans-serif;
  }
  .stage {
    width: 1200px; height: 900px;
    display: flex; flex-direction: column; align-items: center;
    justify-content: center; gap: 56px;
  }
  .card {
    width: 630px; height: 360px; position: relative;
    box-shadow: 0 10px 30px rgba(0,0,0,.55);
  }
  .card--front { background: var(--card-white); }
  .card--back { background: var(--teal); }

  .wordmark {
    font-family: "Poppins", sans-serif; font-weight: 800;
    text-transform: uppercase; line-height: 1;
  }
  .card--front .wordmark {
    position: absolute; top: 44px; right: 48px; width: 330px;
    color: var(--purple); text-align: left;
  }
  .wordmark__name { display: block; font-size: 44px; letter-spacing: -1px; }
  .wordmark__sub { display: block; font-size: 17.5px; letter-spacing: 4.2px; margin-top: 6px; }

  .person { position: absolute; left: 48px; top: 168px; text-align: right; width: 222px; }
  .person__first, .person__last {
    font-family: "Krona One", sans-serif;
    font-size: 19px; text-transform: uppercase; letter-spacing: 0; line-height: 1.25;
  }
  .person__first { color: var(--purple); text-align: left; display: block; }
  .person__last { color: var(--teal); display: block; }
  .person__role {
    display: block; color: var(--purple); font-weight: 400; font-size: 13px;
    letter-spacing: 2.5px; text-transform: uppercase; margin-top: 2px;
  }

  .divider { position: absolute; left: 300px; top: 178px; width: 1px; height: 96px; background: var(--rule); }

  .contacts { position: absolute; left: 322px; top: 176px; list-style: none; }
  .contacts li {
    display: flex; align-items: center; gap: 9px;
    font-size: 13.5px; color: var(--ink); line-height: 24px;
  }
  .contacts svg { width: 14px; height: 14px; fill: none; stroke: var(--purple); stroke-width: 1.8; flex: none; }

  .address { position: absolute; left: 48px; bottom: 34px; font-size: 13.5px; color: var(--ink); }

  .card--back .wordmark {
    position: absolute; left: 50%; top: 118px; transform: translateX(-50%);
    color: #ffffff; text-align: left; width: 330px;
  }
  .back__web {
    position: absolute; left: 0; right: 0; bottom: 56px; text-align: center;
    color: #ffffff; font-size: 15px; font-weight: 500; letter-spacing: .3px;
  }
</style>
</head>
<body>
<main class="stage">
  <section class="card card--front" aria-label="Business card front">
    <div class="wordmark">
      <span class="wordmark__name">RK Bastone</span>
      <span class="wordmark__sub">Construction Inc.</span>
    </div>

    <div class="person">
      <span class="person__first">Rocco</span>
      <span class="person__last">Bastone</span>
      <span class="person__role">Owner</span>
    </div>

    <div class="divider"></div>

    <ul class="contacts">
      <li>
        <svg viewBox="0 0 16 16"><rect x="4" y="1.5" width="8" height="13" rx="1.5"/><line x1="7" y1="12" x2="9" y2="12"/></svg>
        343-555-0142
      </li>
      <li>
        <svg viewBox="0 0 16 16"><path d="M3 2.5l3 .5 1 3-1.5 1.2a8 8 0 0 0 3.3 3.3L10 9l3 1 .5 3c-5.5.5-11-5-10.5-10.5z"/></svg>
        343-555-0187 ext. 348
      </li>
      <li>
        <svg viewBox="0 0 16 16"><rect x="1.5" y="3.5" width="13" height="9"/><path d="M1.5 3.5l6.5 5 6.5-5"/></svg>
        rocco@rkbastoneconst.ca
      </li>
      <li>
        <svg viewBox="0 0 16 16"><circle cx="8" cy="8" r="6.5"/><ellipse cx="8" cy="8" rx="2.8" ry="6.5"/><line x1="1.5" y1="8" x2="14.5" y2="8"/></svg>
        www.rkbastoneconstruction.ca
      </li>
    </ul>

    <p class="address">2180 Fairview Rd, Unit 240, Kingston, ON K7M 4B7</p>
  </section>

  <section class="card card--back" aria-label="Business card back">
    <div class="wordmark">
      <span class="wordmark__name">RK Bastone</span>
      <span class="wordmark__sub">Construction Inc.</span>
    </div>
    <p class="back__web">www.rkbastoneconstruction.ca</p>
  </section>
</main>
</body>
</html>
```